New design for PeopleDesk

We are at the start of the process of evolving an existing business, and have just developed a new logo that will guide the look and feel of the rest of the site.

PeopleDesk.com.au will be the place to go for small business owners that need guidance and tools on how to look after HR functions such as recruitment and performance management amongst other aspects.

The existing site that is going to be evolved in www.hiringcornerfolk.com.au - while some of the content will remain, the entire look of the site needs to change, and a new homepage and other pages need to be developed.

For this project, we'd like the new homepage to be designed to lead the way for how the rest of the pages will look moving forward.

We're looking for a clean, clear and modern design. It should not feel cluttered or busy

The wireframe for the new homepage, and another landing page are attached.

Target Market(s)

Small and medium business owners - slightly male skew

Industry/Entity Type

Small Business

Requirements
Must have
• - Should be clean and simple
- The overall feel from the new logo (attached to the project) should be integrated into all elements of the site
- Should communicate that the site is easy to navigate
- Should communicate that the site is friendly and approachable
- Should communicate that the site is professional (for small businesses)
Nice to have
• This homepage for this site is quite a good design reference in terms of clean design.

http://www.choremoose.com/

For PeopleDesk though, the 3 boxes under the main image should appear above the fold though.

Also, happy for one other colour to be introduced to highlight call to action buttons etc.
Should not have
• Must not be cluttered
Should not introduce more than one additional colour to the existing colours from the logo

```html
<!DOCTYPE html>
<html lang="en">
<head>
<meta charset="utf-8">
<title>PeopleDesk – Homepage</title>
<link rel="stylesheet" href="https://fonts.googleapis.com/css2?family=Bebas+Neue&family=Noto+Serif:wght@400;700&family=Open+Sans:wght@400;600&family=Arimo:wght@400;700&display=swap">
<style>
:root{
  --blue-deep:#0a6fc2;
  --blue:#1594dc;
  --blue-light:#3ab6ee;
  --sky:#e4f5fc;
  --green:#3fbf1c;
  --green-dark:#2c9a0e;
  --grey-bg:#e9e9e9;
  --panel-line:#c9c9c9;
  --text:#555;
  --text-dark:#333;
  --muted:#888;
  --button:#4a97d2;
  --footer:#3a3a3a;
  --footer-bottom:#2f2f2f;
  --footer-text:#cfcfcf;
  --white:#fff;
}
*{box-sizing:border-box;margin:0;padding:0}
html,body{width:1135px;height:1200px;overflow:hidden;background:var(--grey-bg)}
body{font-family:"Arimo",Arial,sans-serif;color:var(--text)}
.page{position:relative;width:1024px;height:1083px;transform:scale(1.1084);transform-origin:0 0;background:var(--grey-bg)}
.abs{position:absolute}

/* header */
.header-band{left:0;top:0;width:1024px;height:372px;background:radial-gradient(ellipse at 50% 40%,var(--blue-light) 0%,var(--blue) 45%,var(--blue-deep) 100%)}
.top-bar{left:0;top:0;width:1024px;height:24px;background:var(--blue-deep);border-bottom:1px solid #4cb7ea}
.account-tab{top:0;height:20px;background:linear-gradient(#f4f9fc,#c9dfee);border-radius:0 0 5px 5px;font-size:11px;color:var(--blue-deep);display:flex;align-items:center;gap:5px;padding:0 10px}
.account-tab i{width:9px;height:9px;border-radius:2px;background:#d9a23c;display:inline-block}
.brand{left:110px;top:46px;display:flex;align-items:center;gap:8px}
.brand-mark{width:40px;height:40px;border-radius:50%;background:var(--white)}
.brand-name{font-family:"Arimo",Arial,sans-serif;font-size:30px;color:var(--white);letter-spacing:-.5px}
.nav{left:400px;top:56px;display:flex;gap:0;font-size:13px;color:var(--white)}
.nav a{color:var(--white);text-decoration:none;text-align:center;line-height:12px;padding:8px 9px;height:32px;display:flex;align-items:center;margin-right:9px}
.nav a.active{background:linear-gradient(#27a7e4,#0f7fc8);border:1px solid #6ccaf3;border-radius:4px}

/* hero */
.hero{left:111px;top:122px;width:802px;height:300px;background:var(--white);padding:2px 7px;box-shadow:0 10px 14px -6px rgba(0,0,0,.25)}
.hero-inner{position:relative;width:100%;height:296px;background:radial-gradient(circle at 60% 55%,#ffffff 0%,var(--sky) 60%,#d0ecf8 100%)}
.guides{left:0;top:0;width:164px;height:296px;background:var(--white)}
.guides h2{font-family:"Bebas Neue",sans-serif;font-weight:400;color:var(--green);font-size:21px;height:38px;line-height:42px;padding-left:8px;background:#fff}
.guides a{display:block;font-family:"Bebas Neue",sans-serif;font-size:15px;color:#555;height:36px;line-height:36px;padding-left:9px;background:linear-gradient(#fafafa,#dcdcdc);border-bottom:1px solid #fff;text-decoration:none}
.tagline{left:190px;top:78px;width:240px;text-align:center}
.tagline h1{font-family:"Bebas Neue",sans-serif;font-weight:400;font-size:32px;color:var(--green)}
.tagline p{font-family:"Bebas Neue",sans-serif;font-size:16px;line-height:19px;color:#667;margin-top:10px;letter-spacing:.3px}
.cta{left:210px;top:208px;width:166px;height:38px;border-radius:6px;background:linear-gradient(#6fdc3a,var(--green) 50%,var(--green-dark));color:var(--white);font-size:16px;font-weight:700;display:flex;align-items:center;justify-content:center;gap:10px;box-shadow:0 3px 4px rgba(0,0,0,.2)}
.video{left:432px;top:38px;width:330px;height:212px;background:#cfcfcf;padding:7px;box-shadow:0 6px 8px -4px rgba(0,0,0,.3)}
.video-screen{width:100%;height:174px;background:var(--white);display:flex;align-items:center;justify-content:center}
.video-controls{height:24px;background:linear-gradient(#fafafa,#dedede);display:flex;align-items:center;font-size:10px;color:#444}
.video-controls span{padding:0 8px}

/* content panel */
.panel{left:111px;top:455px;width:803px;height:305px;background:var(--white);border:1px solid var(--panel-line)}
.col{top:30px;width:244px}
.col h3{font-weight:400;font-size:19px;color:#555;padding-bottom:6px;border-bottom:2px solid #888;display:flex;align-items:center;gap:10px}
.col h3 i{width:17px;height:17px;border:2px solid #bbb;border-radius:50%;display:inline-block}
.col h3 b{width:22px;height:15px;background:#ccc;display:inline-block;border-radius:2px}
.photo{background:linear-gradient(#9a8a7e,#5f5650);border:3px solid #fff;outline:1px solid #ccc}
.about-text{font-size:9.6px;line-height:13.6px;color:var(--muted);letter-spacing:0}
.about-text a{color:var(--blue);text-decoration:none}
.more{width:88px;height:22px;border-radius:11px;background:linear-gradient(#6cb3e6,var(--button));color:var(--white);font-size:11px;display:flex;align-items:center;justify-content:center}
.news-title{font-family:"Noto Serif",serif;font-size:11px;font-weight:700;color:var(--text-dark)}
.news-title.link{text-decoration:underline}
.news-text{font-size:10.5px;line-height:15px;color:#666}
.thumb{width:44px;height:44px;border:1px solid #ccc;padding:3px;background:#fff}
.thumb div{width:100%;height:100%}
.social-row{display:flex;align-items:center;height:34px;font-size:8.5px;color:#666}
.social-dot{width:20px;height:20px;border-radius:50%;background:var(--blue);margin-right:22px}
.chev{margin-left:auto;color:#ccc;font-size:14px}

/* footer */
.footer{left:0;top:800px;width:1024px;height:240px;background:var(--footer)}
.footer-bottom{left:0;top:1040px;width:1024px;height:43px;background:var(--footer-bottom);font-size:9px;color:#777;padding:15px 111px}
.footer h4{font-family:"Noto Serif",serif;font-weight:400;font-size:18px;color:var(--white)}
.flinks a{display:block;height:27px;line-height:27px;border-bottom:1px solid #4a4a4a;font-size:11.5px;color:var(--footer-text);text-decoration:none;padding-left:4px}
.flinks a.current{background:#262626;color:var(--white)}
.tweet{font-family:"Open Sans",sans-serif;font-size:10.5px;line-height:13px;color:var(--footer-text);padding:7px 2px 5px;border-bottom:1px solid #4a4a4a}
.tweet em{font-size:9px}
.find-dot{width:32px;height:32px;border-radius:50%;background:#bdbdbd}
</style>
</head>
<body>
<div class="page">
  <div class="abs header-band"></div>
  <div class="abs top-bar"></div>
  <div class="abs account-tab" style="left:767px"><i></i>Register</div>
  <div class="abs account-tab" style="left:842px;width:72px"><i></i>Login</div>

  <div class="abs brand"><span class="brand-mark"></span><span class="brand-name">PeopleDesk</span></div>

  <nav class="abs nav">
    <a class="active">Attract</a><a>Recruit</a><a>Induction</a><a>Engage</a><a>Performance<br>Management</a><a>Termination &amp;<br>Redundancy</a><a>Community</a>
  </nav>

  <section class="abs hero">
    <div class="hero-inner">
      <div class="abs guides">
        <h2>DIY HowTo Guides –</h2>
        <a>Attract</a><a>Recruit</a><a>Induction</a><a>Engage</a><a>Performance Management</a><a>Termination &amp; Redundancy</a><a>Community</a>
      </div>
      <div class="abs tagline">
        <h1>Tag Line Put Here</h1>
        <p>Pellentesque habitant morbi tristique senectus et netus et malesuada fames ac turpis egestas.</p>
      </div>
      <div class="abs cta">Get Started Now
        <svg width="16" height="16" viewBox="0 0 16 16"><circle cx="8" cy="8" r="8" fill="#fff"/><path d="M4 8h6M8 5l3 3-3 3" stroke="#2c9a0e" stroke-width="2" fill="none"/></svg>
      </div>
      <div class="abs video">
        <div class="video-screen">
          <svg width="86" height="86" viewBox="0 0 86 86"><circle cx="43" cy="43" r="40" fill="none" stroke="#eee" stroke-width="5"/><path d="M37 31l14 12-14 12z" fill="#e4e4e4"/></svg>
        </div>
        <div class="video-controls">
          <span>▶</span><span>🔈</span><span style="padding-left:2px">0:05 / 7:28</span><span style="margin-left:auto">p</span><span>⇄</span><span>⤢</span>
        </div>
      </div>
    </div>
  </section>

  <section class="abs panel">
    <div class="abs col" style="left:16px">
      <h3>About Us <i></i></h3>
      <div class="abs photo" role="img" aria-label="Portrait photo of the founder" style="left:2px;top:44px;width:88px;height:88px"></div>
      <p class="abs about-text" style="left:98px;top:40px;width:148px">Hiring Corner Folk is Australia's first online instructional advice, videos and template resource on conducting an end-to-end, six-step professional recruitment process for small business owners.</p>
      <p class="abs about-text" style="left:0;top:149px;width:246px">A one-stop shop for small business owners, Hiring Corner Folk provides practical steps for small business owners to confidently recruit quality people.</p>
      <p class="abs about-text" style="left:0;top:200px">Founded by <a>Dana Whitfield</a> – a recruitment ...</p>
      <div class="abs more" style="left:2px;top:222px">Learn More</div>
    </div>

    <div class="abs col" style="left:303px;width:216px">
      <h3>News / community <b></b></h3>
      <p class="abs news-title link" style="left:2px;top:44px">Nullam portitor enim id dui</p>
      <div class="abs thumb" style="left:2px;top:64px"><div role="img" aria-label="News article thumbnail photo" style="background:linear-gradient(#a89480,#4c3f36)"></div></div>
      <p class="abs news-text" style="left:54px;top:70px;width:166px">Maecenas vitae felis eu lacus vitae rhoncus pellentesque [...]</p>
      <div class="abs" style="left:2px;top:120px;width:198px;border-top:1px solid #ccc"></div>
      <p class="abs news-title" style="left:2px;top:136px">Nam eget velit purus nam</p>
      <div class="abs thumb" style="left:2px;top:158px"><div role="img" aria-label="Community post thumbnail illustration" style="background:linear-gradient(#7fb8d8,#c05a60)"></div></div>
      <p class="abs news-text" style="left:54px;top:164px;width:166px">Sed adipiscing convallis rhoncis consequat. Nunc semfelis [...]</p>
      <div class="abs more" style="left:2px;top:222px">Learn More</div>
    </div>

    <div class="abs col" style="left:569px;width:218px">
      <h3>SOCIAL <b style="border-radius:50%"></b></h3>
      <div class="abs" style="left:0;top:56px;width:218px">
        <div class="social-row"><span class="social-dot"></span>Lorem ipsum dolor sit amet, consectetur<span class="chev">›</span></div>
        <div class="social-row"><span class="social-dot" style="background:#5ab3e8"></span>Lorem ipsum dolor sit amet, consectetur<span class="chev">›</span></div>
        <div class="social-row"><span class="social-dot" style="background:#333"></span>Lorem ipsum dolor sit amet, consectetur<span class="chev">›</span></div>
        <div class="social-row"><span class="social-dot" style="background:#c8312b"></span>Lorem ipsum dolor sit amet, consectetur<span class="chev">›</span></div>
      </div>
      <div class="abs more" style="left:2px;top:222px">Learn More</div>
    </div>
  </section>

  <footer class="abs footer">
    <h4 class="abs" style="left:111px;top:36px">Company</h4>
    <div class="abs flinks" style="left:111px;top:78px;width:175px">
      <a class="current">Home</a><a>Attract</a><a>Contact</a><a>Recruit</a>
    </div>
    <div class="abs flinks" style="left:321px;top:78px;width:170px">
      <a>Induction</a><a>Engage</a><a>Performance &amp; Management</a><a>Termination &amp; Redundancy</a>
    </div>
    <h4 class="abs" style="left:563px;top:36px">Recent Tweets</h4>
    <div class="abs" style="left:563px;top:80px;width:172px">
      <p class="tweet">@Username, Lorem ipsum dolor sit amet, consectetr - <em>9 hours ago</em></p>
      <p class="tweet">@Username, Lorem ipsum dolor sit amet, consectetr - <em>9 hours ago</em></p>
      <p class="tweet">@Username, Lorem ipsum dolor sit amet, consectetr - <em>9 hours ago</em></p>
    </div>
    <h4 class="abs" style="left:808px;top:32px">Find us on</h4>
    <div class="abs" style="left:806px;top:78px;display:flex;gap:7px">
      <span class="find-dot"></span><span class="find-dot"></span><span class="find-dot"></span>
    </div>
  </footer>
  <div class="abs footer-bottom">Copyright @ 2011. All rights reserved by PeopleDesk Recruit</div>
</div>
</body>
</html>
```